Website design for a Fine Food exhibition in Asia

We need a website design for a Food and Wine exhibition (home page). The name of the exhibition is "Savorix" which is going to be Held in south korea. The concept is "Fine Food" in major, qui means clustering Would not we accept Any canned food, fast food, chips, thesis kind of foods. We do not open to the public like Some Other Food exhibitions do, Then only trade visitors. The EXHIBITORS will come from all the World. The categories we Would like to make is in attachment below. We will update the text When the category's share will be done. We need a color can qui correspond well to the "Find Food ', color of our logo qui est in attachment Would be good. You can offer us some photos, images, like photos of fine food corners in supermarkets, gourmet shops like photos of etc. ... You can find links Some of "same" exhibitions in below, qui can give you a guideline of the kind of website we expect. http://en.plumbarrow-fairhall.com/ http://velmontrade.com/ http: //www.tarnicplaza. co.kr We will ask to the winning designer to Develop the full website under Wordpress.
Updates

Project Deadline Extended
Reason: Because we need some modifications to requests.

Target Market(s)

Fine food, gourmet food, "grocery", pastry, bakery

Number of Pages Required

5+ page

Font styles to use
Sans Serif

Colors
886aae
6b449b
e34197
e667a6
9bcb3c
f58947
f37122
ec1f27

Requirements
Must have
• Warm colors, and layout showing the high level of foods, fine foods, gourmet foods
Nice to have
• It would be nice to include the sentence "The new meeting place for the gourmet food in Asia"

```html
<!DOCTYPE html>
<html lang="en">
<head>
<meta charset="utf-8">
<title>Savorix – The Fine Food Event in Asia</title>
<link href="https://fonts.googleapis.com/css2?family=Oswald:wght@400;500&family=Roboto:wght@300;400;500;700&display=swap" rel="stylesheet">
<style>
:root{
  --plum:#5e0f62;
  --plum-mid:#6b1a70;
  --plum-box:rgba(92,20,96,.78);
  --red:#c8102e;
  --ink:#333;
  --muted:#666;
  --line:#dcdcdc;
  --light:#f2f2f2;
  --white:#fff;
  --dark:#2b2b2b;
}
*{box-sizing:border-box;margin:0;padding:0}
html,body{width:1200px;height:3010px;overflow:hidden}
body{font-family:"Roboto",Arial,sans-serif;color:var(--ink);background:var(--white);position:relative}
.oswald{font-family:"Oswald","Arial Narrow",sans-serif}

/* top bar */
.topbar{height:32px;background:var(--plum);color:var(--white);font-size:11px;display:flex;align-items:center;padding:0 96px}
.topbar .lang{display:flex;align-items:center;gap:6px}
.topbar .lang i{width:14px;height:9px;background:#c8c8d8;display:inline-block}
.topbar .contact{margin-left:auto;display:flex;gap:34px;align-items:center;font-size:12px}
.topbar .contact span{display:flex;align-items:center;gap:8px}
.topbar .social{display:flex;gap:6px;margin-left:30px}
.topbar .social i{width:17px;height:17px;border-radius:50%;background:var(--white);display:block}

/* header */
.header{height:102px;display:flex;align-items:center;padding:0 96px;box-shadow:0 2px 4px rgba(0,0,0,.06);position:relative;z-index:2}
.brand{display:flex;flex-direction:column}
.brand .name{display:flex;align-items:center;gap:10px;font-size:38px;font-weight:700;color:var(--plum-mid);letter-spacing:1px}
.brand .name i{width:16px;height:16px;border-radius:50%;background:var(--plum-mid);display:block}
.brand .tag{font-size:12.5px;color:var(--red);margin-top:2px}
.nav{margin-left:auto;display:flex;gap:36px;align-items:center;font-size:12.5px;color:#333;font-weight:500}
.nav a{color:inherit;text-decoration:none}
.nav a.active{color:var(--plum-mid)}

/* hero */
.hero{position:absolute;top:134px;left:0;width:1200px;height:552px;background:radial-gradient(ellipse at 58% 35%,#e9a277 0%,#c98a5e 22%,#8e7a55 45%,#5b6a3c 70%,#3d4a2c 100%)}
.hero h1{position:absolute;top:190px;width:100%;text-align:center;color:var(--white);font-family:"Oswald","Arial Narrow",sans-serif;font-weight:500;line-height:1.15;text-shadow:0 2px 6px rgba(0,0,0,.35)}
.hero h1 .l1{display:block;font-size:44px}
.hero h1 .l2{display:block;font-size:40px}
.dots{position:absolute;top:300px;left:0;width:100%;display:flex;justify-content:center;gap:8px}
.dots i{width:11px;height:11px;border-radius:50%;background:var(--white);display:block}
.dots i.on{background:transparent;border:2px solid var(--white)}
.facts{position:absolute;top:434px;left:98px;display:flex;gap:54px}
.fact{height:94px;background:var(--plum-box);outline:2px solid rgba(255,255,255,.35);outline-offset:-6px;display:flex;align-items:center;padding:0 24px;gap:16px;color:var(--white)}
.fact.w1{width:314px}.fact.w2{width:290px}.fact.w3{width:316px}
.fact h3{font-family:"Oswald","Arial Narrow",sans-serif;font-weight:400;font-size:15px;margin-bottom:4px}
.fact p{font-size:12px;line-height:1.5}

/* about */
.about{position:absolute;top:686px;left:0;width:1200px;height:572px}
.section-title{text-align:center;font-size:32px;font-weight:400;color:#333;letter-spacing:.5px}
.about .section-title{margin-top:72px}
.divider{display:flex;justify-content:center;align-items:center;gap:14px;margin-top:12px}
.divider span{width:96px;height:1px;background:#bbb}
.divider i{width:10px;height:10px;border:1px solid #888;border-radius:50%;display:block}
.about p.lead{width:900px;margin:24px auto 0;text-align:center;font-size:11.5px;line-height:22px;color:var(--muted)}
.cards{position:absolute;top:276px;left:98px;display:flex;gap:24px}
.card{width:318px;height:214px;position:relative;color:var(--white);text-align:center}
.card .ph{position:absolute;inset:0}
.card .frame{position:absolute;inset:10px;border:1px solid rgba(255,255,255,.8)}
.card .txt{position:absolute;top:84px;width:100%}
.card .txt small{display:block;width:10px;height:10px;margin:0 auto 6px;border:1px solid #fff;border-radius:50%}
.card h4{font-size:21px;font-weight:400}
.card p{font-size:13px;margin-top:4px}

/* split */
.split{position:absolute;top:1258px;left:0;width:1200px;height:490px;display:flex}
.half{width:600px;height:490px;position:relative;text-align:center}
.half.exh{background:linear-gradient(160deg,#3a302a 0%,#1e1b18 55%,#2b241e 100%);color:var(--white)}
.half.vis{background:linear-gradient(160deg,#e4e1df 0%,#f0eae4 45%,#d9cfc5 100%);color:#333}
.half .badge{position:absolute;top:132px;left:250px;width:100px;height:100px;border-radius:50%;display:flex;align-items:center;justify-content:center}
.half.exh .badge{border:7px solid var(--white)}
.half.vis .badge{border:7px solid var(--plum-mid)}
.half h3{position:absolute;top:264px;width:100%;font-size:19px;font-weight:400}
.half p{position:absolute;top:300px;left:160px;width:280px;font-size:11px;line-height:20px}
.btn{display:inline-block;background:var(--red);color:var(--white);font-size:11px;font-weight:500;padding:0 18px;height:34px;line-height:34px;text-decoration:none}
.half .btn{position:absolute;top:378px;left:50%;transform:translateX(-50%)}

/* news */
.news{position:absolute;top:1748px;left:0;width:1200px;height:632px}
.news .section-title{margin-top:68px}
.news-grid{position:absolute;top:138px;left:98px;display:grid;grid-template-columns:490px 490px;gap:22px 22px}
.post{height:212px;border:1px solid var(--line);display:flex;background:#fbfbfb}
.post .ph{width:190px;height:210px;flex:none}
.post .body{padding:22px 20px 0 22px}
.post h4{font-size:15.5px;font-weight:400;color:#444}
.post .meta{display:flex;align-items:center;gap:14px;margin-top:12px;font-size:11px;color:#666}
.post .date{background:var(--red);color:var(--white);font-weight:700;padding:4px 8px;font-size:11px}
.post .meta em{font-style:italic}
.post p{font-size:11px;line-height:18px;color:#555;margin-top:10px}
.post .more{font-size:12px;color:#333;margin-top:8px;display:block}

/* newsletter */
.newsletter{position:absolute;top:2414px;left:194px;width:810px;height:60px;display:flex;align-items:center}
.newsletter .ico{width:56px;height:56px;border-radius:50%;background:var(--red);display:flex;align-items:center;justify-content:center;flex:none}
.newsletter .copy{margin-left:18px;width:312px}
.newsletter h3{font-family:"Oswald","Arial Narrow",sans-serif;font-weight:400;font-size:24px;color:#333}
.newsletter p{font-size:15px;color:#555}
.newsletter .field{width:312px;height:46px;border:1px solid var(--line);font-size:12px;color:#777;padding:0 12px;display:flex;align-items:center}
.newsletter .btn{height:46px;line-height:46px;font-size:14px;padding:0 28px}

/* partners */
.partners{position:absolute;top:2544px;left:0;width:1200px;height:108px;background:var(--light);border-top:1px solid #e2e2e2;display:flex;align-items:center;justify-content:center;gap:78px}
.partners i{display:block;height:30px;background:#b4b4b4;border-radius:3px}

/* footer */
.footer{position:absolute;top:2652px;left:0;width:1200px;height:296px;background:var(--plum-mid);color:var(--white)}
.footer .flogo{position:absolute;top:56px;left:138px;width:126px;height:126px;border-radius:50%;background:var(--white);display:flex;align-items:center;justify-content:center;color:var(--plum-mid);font-weight:700;font-size:24px}
.footer .fsocial{position:absolute;top:196px;left:140px;display:flex;gap:8px}
.footer .fsocial i{width:26px;height:26px;border-radius:50%;border:2px solid var(--white);display:block}
.col{position:absolute;top:52px}
.col h4{font-size:18px;font-weight:500;margin-bottom:22px;letter-spacing:.3px}
.col ul{list-style:none;font-size:11.5px}
.col li{height:26px;display:flex;align-items:center;gap:8px}
.col li::before{content:"›";font-size:14px}
.col.contact li::before{content:none}
.col.contact li{height:auto;align-items:flex-start;gap:16px;margin-bottom:18px;font-size:13px;line-height:20px}
.copyright{position:absolute;top:2948px;left:0;width:1200px;height:62px;background:var(--dark);color:#ddd;font-size:12px;display:flex;align-items:center;justify-content:center}
</style>
</head>
<body>

<div class="topbar">
  <div class="lang"><i></i>ENGLISH ⌄</div>
  <div class="contact">
    <span><svg width="12" height="12" viewBox="0 0 24 24" fill="#fff"><path d="M6.6 10.8c1.4 2.8 3.8 5.1 6.6 6.6l2.2-2.2c.3-.3.7-.4 1-.2 1.1.4 2.3.6 3.6.6.6 0 1 .4 1 1V20c0 .6-.4 1-1 1C10.6 21 3 13.4 3 4c0-.6.4-1 1-1h3.5c.6 0 1 .4 1 1 0 1.3.2 2.5.6 3.6.1.3 0 .7-.2 1z"/></svg>503-555-0148</span>
    <span><svg width="14" height="11" viewBox="0 0 24 18" fill="none" stroke="#fff" stroke-width="2"><rect x="1" y="1" width="22" height="16"/><path d="M1 1l11 9 11-9"/></svg>customerservice@savorix.com</span>
  </div>
  <div class="social"><i></i><i></i><i></i><i></i></div>
</div>

<header class="header">
  <div class="brand">
    <div class="name"><i></i>Savorix</div>
    <div class="tag">The Fine Food Event in Asia</div>
  </div>
  <nav class="nav">
    <a class="active" href="#">HOME</a><a href="#">THE EXHIBITION</a><a href="#">EXHIBITORS</a><a href="#">VISITORS</a><a href="#">EVENTS</a><a href="#">MEDIA</a><a href="#">CONTACT</a>
    <svg width="14" height="14" viewBox="0 0 24 24" fill="none" stroke="#333" stroke-width="3"><circle cx="10" cy="10" r="7"/><path d="M15 15l7 7"/></svg>
  </nav>
</header>

<section class="hero" role="img" aria-label="Plated salmon fillet with broccoli, carrots and rice">
  <h1><span class="l1">THE NEW MEETING PLACE FOR</span><span class="l2">The Gourmet Food In Asia</span></h1>
  <div class="dots"><i class="on"></i><i></i><i></i><i></i></div>
  <div class="facts">
    <div class="fact w1">
      <svg width="38" height="38" viewBox="0 0 24 24" fill="#fff"><path d="M4 4h16v17H4z" fill="none" stroke="#fff" stroke-width="2"/><rect x="4" y="4" width="16" height="4"/><rect x="7" y="2" width="2" height="4"/><rect x="15" y="2" width="2" height="4"/><rect x="7" y="11" width="2" height="2"/><rect x="11" y="11" width="2" height="2"/><rect x="15" y="11" width="2" height="2"/><rect x="7" y="15" width="2" height="2"/><rect x="11" y="15" width="2" height="2"/></svg>
      <div><h3>WHEN</h3><p>November 01-03, 2017<br>Wednesday To Friday</p></div>
    </div>
    <div class="fact w2">
      <svg width="40" height="40" viewBox="0 0 24 24"><circle cx="12" cy="12" r="10" fill="#fff"/><path d="M7 6c2 1 3 3 2 5s1 3 3 3 1 3 0 5M14 4c0 2 2 3 4 3" stroke="#5e0f62" stroke-width="1.6" fill="none"/></svg>
      <div><h3>VENUE</h3><p>Hanvale Hall 8b<br>Hanvale Expo, Seoul, South Korea</p></div>
    </div>
    <div class="fact w3">
      <svg width="40" height="40" viewBox="0 0 24 24"><circle cx="12" cy="12" r="10" fill="#fff"/><path d="M12 6v6l4 2" stroke="#5e0f62" stroke-width="2" fill="none"/></svg>
      <div><h3>OPENING TIMES</h3><p>10:00 – 18:00 for the first day<br>10:00 – 17:00 for the second day</p></div>
    </div>
  </div>
</section>

<section class="about">
  <h2 class="section-title">ABOUT SAVORIX</h2>
  <div class="divider"><span></span><i></i><span></span></div>
  <p class="lead">Nemo enim ipsam voluptatem quia voluptas sit aspernatur aut odit aut fugit, sed quia consequuntur magni dolores eos qui ratione voluptatem sequi nesciunt. Neque porro quisquam est, qui dolorem ipsum quia dolor sit amet, consectetur, adipisci velit, sed quia non numquam eius modi tempora incidunt ut labore et dolore magnam aliquam quaerat voluptatem. Ut enim ad minima veniam, quis nostrum exercitationem ullam corporis suscipit laboriosam, nisi ut aliquid</p>
  <div class="cards">
    <div class="card"><div class="ph" role="img" aria-label="Guests dining at the food exhibition" style="background:linear-gradient(135deg,#4a2c22,#2a1c18 60%,#6b3f2a)"></div><div class="frame"></div><div class="txt"><small></small><h4>Food Exhibition</h4><p>Nemo enim ipsam</p></div></div>
    <div class="card"><div class="ph" role="img" aria-label="Busy restaurant floor with warm lights" style="background:linear-gradient(135deg,#3c2a20,#6e4a2e 50%,#2d2018)"></div><div class="frame"></div><div class="txt"><small></small><h4>Floor Plan</h4><p>Nemo enim ipsam</p></div></div>
    <div class="card"><div class="ph" role="img" aria-label="Table set with gourmet dishes" style="background:linear-gradient(135deg,#5a3a22,#8a5a34 50%,#3a2618)"></div><div class="frame"></div><div class="txt"><small></small><h4>Asian VIP buyers</h4><p>Nemo enim ipsam</p></div></div>
  </div>
</section>

<section class="split">
  <div class="half exh" role="img" aria-label="Dark wooden table with pasta dishes">
    <div class="badge"><svg width="40" height="32" viewBox="0 0 24 18" fill="none" stroke="#fff" stroke-width="2"><rect x="1" y="1" width="22" height="16"/><rect x="4" y="4" width="7" height="6" fill="#fff"/><path d="M14 5h6M14 9h6M4 13h16"/></svg></div>
    <h3>Who Are The Exhibitors?</h3>
    <p>Sed ut perspiciatis uSed ut perspiciatis unde omnis iste natus error sit voluptatem accusantium doloremque laudantium, totam rem aperiam, eaque ipsa quae ab illo inventore</p>
    <a class="btn" href="#">REGISTER NOW ➜</a>
  </div>
  <div class="half vis" role="img" aria-label="Soft light scene of a visitor at the fair">
    <div class="badge" style="background:var(--plum-mid);border-color:var(--plum-mid)"><div style="width:72px;height:72px;border-radius:50%;background:#fff;display:flex;align-items:center;justify-content:center"><svg width="36" height="30" viewBox="0 0 24 20" fill="#6b1a70"><circle cx="12" cy="5" r="3.5"/><circle cx="5" cy="7" r="2.5"/><circle cx="19" cy="7" r="2.5"/><path d="M6 18c0-4 3-7 6-7s6 3 6 7z"/><path d="M0 17c0-3 2-5 5-5 1 0 2 .3 2 .5-1 1.5-1.5 3-1.5 4.5zM24 17c0-3-2-5-5-5-1 0-2 .3-2 .5 1 1.5 1.5 3 1.5 4.5z"/></svg></div></div>
    <h3>Who Are The Visitors?</h3>
    <p>Sed ut perspiciatis uSed ut perspiciatis unde omnis iste natus error sit voluptatem accusantium doloremque laudantium, totam rem aperiam, eaque ipsa quae ab illo inventore</p>
    <a class="btn" href="#">REGISTER NOW ➜</a>
  </div>
</section>

<section class="news">
  <h2 class="section-title">RECENT NEWS</h2>
  <div class="news-grid">
    <article class="post"><div class="ph" role="img" aria-label="Bread and charcuterie board" style="background:linear-gradient(135deg,#8a5a38,#c89a6a 50%,#5a3a26)"></div><div class="body"><h4>Sed ut perspiciatis unde omnis</h4><div class="meta"><span class="date">MAY 25, 2016</span><em>💬 2 comments</em></div><p>Nulla at diam ornare, aliquam urna vel, commodo urna. Nam id risus a est luctus consectetur quis eget libero. Suspendisse potenti. Pellentesque habitant morbi tristique senectus</p><span class="more">Read More +</span></div></article>
    <article class="post"><div class="ph" role="img" aria-label="Seafood platter on a dark table" style="background:linear-gradient(135deg,#3a3430,#9a6a4a 50%,#2a2420)"></div><div class="body"><h4>Sed ut perspiciatis unde omnis</h4><div class="meta"><span class="date">MAY 25, 2016</span><em>💬 2 comments</em></div><p>Nulla at diam ornare, aliquam urna vel, commodo urna. Nam id risus a est luctus consectetur quis eget libero. Suspendisse potenti. Pellentesque habitant morbi tristique senectus</p><span class="more">Read More +</span></div></article>
    <article class="post"><div class="ph" role="img" aria-label="Roasted meat with vegetables on a board" style="background:linear-gradient(135deg,#6a4a30,#b87a4a 50%,#4a6a2a)"></div><div class="body"><h4>Sed ut perspiciatis unde omnis</h4><div class="meta"><span class="date">MAY 25, 2016</span><em>💬 2 comments</em></div><p>Nulla at diam ornare, aliquam urna vel, commodo urna. Nam id risus a est luctus consectetur quis eget libero. Suspendisse potenti. Pellentesque habitant morbi tristique senectus</p><span class="more">Read More +</span></div></article>
    <article class="post"><div class="ph" role="img" aria-label="Braised beef with potatoes" style="background:linear-gradient(135deg,#2a2018,#7a4a28 50%,#c8a050)"></div><div class="body"><h4>Sed ut perspiciatis unde omnis</h4><div class="meta"><span class="date">MAY 25, 2016</span><em>💬 2 comments</em></div><p>Nulla at diam ornare, aliquam urna vel, commodo urna. Nam id risus a est luctus consectetur quis eget libero. Suspendisse potenti. Pellentesque habitant morbi tristique senectus</p><span class="more">Read More +</span></div></article>
  </div>
</section>

<section class="newsletter">
  <div class="ico"><svg width="24" height="18" viewBox="0 0 24 18" fill="none" stroke="#fff" stroke-width="2"><rect x="1" y="1" width="22" height="16" rx="2"/><path d="M1 2l11 8 11-8"/></svg></div>
  <div class="copy"><h3>Join our Newsletter.</h3><p>Stay up to date with the latest news.</p></div>
  <div class="field">Name</div>
  <a class="btn" href="#">SUBSCRIBE</a>
</section>

<section class="partners" aria-label="Partners">
  <i style="width:64px"></i><i style="width:112px"></i><i style="width:110px"></i><i style="width:108px"></i><i style="width:82px"></i><i style="width:98px"></i>
</section>

<footer class="footer">
  <div class="flogo">Savorix</div>
  <div class="fsocial"><i></i><i></i><i></i><i></i></div>
  <div class="col contact" style="left:372px">
    <h4>CONTACT US</h4>
    <ul>
      <li><svg width="16" height="20" viewBox="0 0 16 20" fill="none" stroke="#fff" stroke-width="1.6"><path d="M8 19s6-6.5 6-11A6 6 0 0 0 2 8c0 4.5 6 11 6 11z"/><circle cx="8" cy="8" r="2.2"/></svg><span>Savorix<br>2210 Orchard Crest Ave Suite 410<br>Linmoor, TX 75190</span></li>
      <li><svg width="18" height="18" viewBox="0 0 24 24" fill="none" stroke="#fff" stroke-width="1.6"><path d="M6.6 10.8c1.4 2.8 3.8 5.1 6.6 6.6l2.2-2.2c.3-.3.7-.4 1-.2 1.1.4 2.3.6 3.6.6.6 0 1 .4 1 1V20c0 .6-.4 1-1 1C10.6 21 3 13.4 3 4c0-.6.4-1 1-1h3.5c.6 0 1 .4 1 1 0 1.3.2 2.5.6 3.6.1.3 0 .7-.2 1z"/></svg><span>Phone: (904) 555-0193</span></li>
      <li><svg width="18" height="14" viewBox="0 0 24 18" fill="none" stroke="#fff" stroke-width="1.6"><rect x="1" y="1" width="22" height="16"/><path d="M1 1l11 9 11-9"/></svg><span>E-Mail: info@savorix.com</span></li>
    </ul>
  </div>
  <div class="col" style="left:678px">
    <h4>FOR EXHIBITORS</h4>
    <ul><li>Exhibitor Registration</li><li>Exhibitor Profile</li><li>Booth Options</li><li>Promote Your Booth</li><li>Official Subcontractors</li><li>Forms &amp; Manuals</li></ul>
  </div>
  <div class="col" style="left:926px">
    <h4>FOR VISITORS</h4>
    <ul><li>Importer</li><li>Distributor</li><li>Hotel and Restaurant</li><li>Retail</li><li>Super/Hypermarket</li><li>Department stores</li></ul>
  </div>
</footer>

<div class="copyright">Copyright © Savorix 2016. All Rights Reserved.</div>

</body>
</html>
```